Heronby Mortgage Capital Business Card

We need a business card design for our mortgage servicing company. In addition to servicing the loans of homeowners, we help homeowners with purchasing their homes and any mortgage refinancing. We would like to see designs that use the colors in the logo attached below (gold-ish yellow and navy blue), and any other design you deem fit! The design should communicate a simpler life with smart mortgages provided by Heronby.

```html
<!DOCTYPE html>
<html lang="en">
<head>
<meta charset="utf-8">
<title>Heronby Mortgage Capital – Business Card</title>
<link rel="stylesheet" href="https://fonts.googleapis.com/css2?family=Montserrat:wght@700&family=Open+Sans:wght@400;600&display=swap">
<style>
  :root {
    --stage: #222222;
    --navy: #271f54;
    --navy-deep: #1c1640;
    --gold: #e3b23c;
    --white: #ffffff;
  }
  * { margin: 0; padding: 0; box-sizing: border-box; }
  html, body { width: 1200px; height: 780px; overflow: hidden; }
  body {
    background: var(--stage);
    position: relative;
    font-family: "Open Sans", sans-serif;
  }
  .card {
    position: absolute;
    top: 230px;
    width: 560px;
    height: 320px;
    background: var(--navy);
    overflow: hidden;
  }
  .card--back { left: 27px; }
  .card--front { left: 613px; }

  .wordmark {
    position: absolute;
    font-family: "Montserrat", sans-serif;
    font-weight: 700;
    white-space: nowrap;
  }
  .back-mark {
    left: 0; right: 0; top: 128px;
    text-align: center;
    font-size: 52px;
    color: var(--navy-deep);
  }
  .front-mark {
    left: 58px; top: 48px;
    font-size: 34px;
    color: var(--gold);
  }
  .wordmark-dot {
    display: inline-block;
    width: 14px; height: 14px;
    background: var(--gold);
    border-radius: 50%;
    margin-right: 12px;
    vertical-align: middle;
  }
  .side-mark {
    right: 22px; top: 36px;
    writing-mode: vertical-rl;
    font-size: 26px;
    color: var(--navy-deep);
  }

  .identity {
    position: absolute;
    left: 0; top: 150px;
    display: flex;
  }
  .identity-bar {
    width: 36px; height: 52px;
    background: var(--gold);
    margin-right: 14px;
  }
  .person-name {
    font-family: "Montserrat", sans-serif;
    font-weight: 700;
    font-size: 30px;
    line-height: 1.05;
    color: var(--gold);
  }
  .person-role {
    font-size: 15px;
    color: var(--white);
    margin-top: 2px;
  }
  .address {
    position: absolute;
    left: 50px; top: 216px;
    font-size: 14px;
    line-height: 1.3;
    color: var(--white);
  }
  .contacts {
    position: absolute;
    left: 50px; top: 256px;
    list-style: none;
    font-size: 14px;
    line-height: 1.3;
    color: var(--white);
  }
  .contacts li { display: flex; align-items: center; gap: 8px; }
  .contacts svg { width: 13px; height: 13px; fill: var(--gold); flex: none; }
</style>
</head>
<body>
  <section class="card card--back" aria-label="Card back">
    <div class="wordmark back-mark">Heronby Mortgage</div>
  </section>

  <section class="card card--front" aria-label="Card front">
    <div class="wordmark front-mark"><span class="wordmark-dot"></span>Heronby Mortgage</div>

    <div class="identity">
      <div class="identity-bar"></div>
      <div>
        <h1 class="person-name">Dana Whitcombe</h1>
        <p class="person-role">Co-Founder</p>
      </div>
    </div>

    <p class="address">4170 Larkspur Ave. Suite 310<br>Denton, TX 76201</p>

    <ul class="contacts">
      <li>
        <svg viewBox="0 0 24 24" aria-hidden="true"><path d="M6.6 10.8a15.1 15.1 0 0 0 6.6 6.6l2.2-2.2a1 1 0 0 1 1-.25 11.4 11.4 0 0 0 3.6.57 1 1 0 0 1 1 1V20a1 1 0 0 1-1 1A17 17 0 0 1 3 4a1 1 0 0 1 1-1h3.5a1 1 0 0 1 1 1c0 1.25.2 2.45.57 3.57a1 1 0 0 1-.25 1z"/></svg>
        (940) 555-0184
      </li>
      <li>
        <svg viewBox="0 0 24 24" aria-hidden="true"><path d="M2 5h20v14H2zm2 2v.5l8 5 8-5V7zm0 2.8V17h16V9.8l-8 5z"/></svg>
        info@website.com
      </li>
      <li>
        <svg viewBox="0 0 24 24" aria-hidden="true"><path d="M12 2a10 10 0 1 0 0 20 10 10 0 0 0 0-20zm6.9 6h-3a15.6 15.6 0 0 0-1.3-3.9A8 8 0 0 1 18.9 8zM12 4a13.8 13.8 0 0 1 1.9 4h-3.8A13.8 13.8 0 0 1 12 4zM4.3 14a8 8 0 0 1 0-4h3.4a16.5 16.5 0 0 0 0 4zm.8 2h3a15.6 15.6 0 0 0 1.3 3.9A8 8 0 0 1 5.1 16zm3-8h-3a8 8 0 0 1 4.3-3.9A15.6 15.6 0 0 0 8.1 8zM12 20a13.8 13.8 0 0 1-1.9-4h3.8A13.8 13.8 0 0 1 12 20zm2.3-6H9.7a14.7 14.7 0 0 1 0-4h4.6a14.7 14.7 0 0 1 0 4zm.3 5.9a15.6 15.6 0 0 0 1.3-3.9h3a8 8 0 0 1-4.3 3.9zm1.7-5.9a16.5 16.5 0 0 0 0-4h3.4a8 8 0 0 1 0 4z"/></svg>
        www.website.com
      </li>
    </ul>

    <div class="wordmark side-mark">Heronby Mortgage</div>
  </section>
</body>
</html>
```